Stationery Design Project - Professional Training Company

Full set of statinery in PDF and format that can be given to the printers

Letterhead
Business cards x 3
Compliments slip
Envelope
Updates

Many thanks for all your contributions, the quality of the designs is amazing.

Thank you all so much for your contribution to this project, I am very impressed with the designs and choice of designs, you are all clearly very talented individuals.

I hope to be making a decision on the final choice this evening UAE time.

Best regards and again thank you so much

Desmond

I would like to take this opportunity to thank you all for your contributions, I have been very impressed with each of the designs submitted.

I will shortly go back and give each of you a personal rating on each of your designs.

Again thank you all so much for your efforts

Best Regards

Desmond

Target Market(s)

We are a training company that provides IT training for Medical and Professional Staff, we train professional adults

Industry/Entity Type

Business

Requirements
Must have
• The letterhead and compliments slip must have at the bottom of the page:-

Bright Harbor Learning LLP operates as a limited liability partnership registered in England and Wales (with registered number OC742168)

Business Cards are to be made up for three people (details of those to be provided after appoval of design but are included in this project) and should contain:

Name
Title
Telephone
email
Address: P.O. Box 518243 Dubai UAE
web address: www.brightharborlearning.example
Nice to have
• Very clean and professional looking
Should not have
• No look to busy or ovr crowded

```html
<!DOCTYPE html>
<html lang="en">
<head>
<meta charset="utf-8">
<title>Bright Harbor Learning – Stationery Set</title>
<link rel="stylesheet" href="https://fonts.googleapis.com/css2?family=Open+Sans:wght@400;600;700&display=swap">
<style>
  :root {
    --backdrop: #e6d9ec;
    --paper: #ffffff;
    --ink: #231f20;
    --ink-soft: #4a4a4a;
    --plum: #4e1249;
    --plum-mark: #7b2c70;
    --green-tint: #dcefdc;
    --plum-tint: #eddcea;
    --shadow: 3px 4px 6px rgba(0,0,0,.35);
  }
  * { box-sizing: border-box; margin: 0; padding: 0; }
  html, body { width: 1200px; height: 844px; overflow: hidden; }
  body {
    background: var(--backdrop);
    font-family: "Open Sans", Arial, sans-serif;
    color: var(--ink);
    position: relative;
  }
  .sheet { position: absolute; background: var(--paper); box-shadow: var(--shadow); overflow: hidden; }

  .brand { display: flex; align-items: center; gap: 8px; position: absolute; }
  .brand-dot { border-radius: 50%; background: var(--plum-mark); flex: none; }
  .brand-name { font-weight: 600; color: var(--ink); white-space: nowrap; line-height: 1; }

  .decor {
    position: absolute; border-radius: 50%;
    background: radial-gradient(circle at 35% 60%, var(--green-tint), var(--plum-tint) 75%);
    opacity: .55;
  }

  /* Letterhead */
  .letterhead { left: 623px; top: 32px; width: 541px; height: 766px; }
  .letterhead .brand { left: 48px; top: 52px; }
  .letterhead .brand-dot { width: 30px; height: 30px; }
  .letterhead .brand-name { font-size: 24px; }
  .letterhead .rule { position: absolute; left: 48px; width: 442px; height: 2px; background: var(--ink); }
  .letterhead .rule-top { top: 108px; }
  .letterhead .rule-bottom { top: 677px; }
  .letterhead .address, .letterhead .contact {
    position: absolute; top: 117px; font-size: 10.5px; line-height: 1.3; color: var(--ink-soft);
  }
  .letterhead .address { left: 48px; }
  .letterhead .contact { right: 51px; text-align: right; }
  .letterhead .decor { left: 110px; top: 250px; width: 320px; height: 300px; }
  .letterhead .web {
    position: absolute; top: 660px; left: 48px; width: 442px; text-align: center;
    font-size: 10.5px; color: var(--ink-soft);
  }
  .letterhead .legal {
    position: absolute; top: 684px; left: 48px; width: 442px; font-size: 7.5px; line-height: 1.3; color: var(--ink-soft);
  }

  /* Business card */
  .card { left: 369px; top: 50px; width: 286px; height: 186px; }
  .card .brand { left: 16px; top: 16px; gap: 6px; }
  .card .brand-dot { width: 18px; height: 18px; }
  .card .brand-name { font-size: 14px; }
  .card .address {
    position: absolute; right: 16px; top: 48px; text-align: right; font-size: 11px; line-height: 1.3; color: var(--ink-soft);
  }
  .card .person { position: absolute; left: 20px; top: 84px; }
  .card .person-name { font-size: 13px; font-weight: 700; }
  .card .person-tel { font-size: 12.5px; margin-top: 3px; }
  .card .person-email { font-size: 10.5px; color: var(--ink-soft); margin-top: 3px; }
  .card .band {
    position: absolute; left: 0; bottom: 0; width: 100%; height: 28px; background: var(--plum);
    color: #fff; font-size: 10px; font-weight: 600; text-align: center; line-height: 28px;
  }

  /* Compliments slip */
  .slip { left: 176px; top: 248px; width: 479px; height: 228px; }
  .slip .decor { left: -40px; top: -50px; width: 220px; height: 200px; }
  .slip .greeting { position: absolute; left: 140px; top: 86px; font-size: 15px; }
  .slip .greeting strong { font-weight: 600; }
  .slip .brand { right: 16px; top: 160px; gap: 6px; }
  .slip .brand-dot { width: 20px; height: 20px; }
  .slip .brand-name { font-size: 14.5px; }
  .slip .legal {
    position: absolute; left: 0; width: 100%; top: 210px; text-align: center; font-size: 6px; color: var(--ink-soft);
  }

  /* Envelope */
  .envelope { left: 36px; top: 488px; width: 622px; height: 310px; }
  .envelope .brand { left: 20px; top: 24px; gap: 7px; }
  .envelope .brand-dot { width: 24px; height: 24px; }
  .envelope .brand-name { font-size: 17px; }
  .envelope .address { position: absolute; left: 26px; top: 70px; font-size: 12px; line-height: 1.3; color: var(--ink-soft); }
  .envelope .decor { left: 470px; top: 160px; width: 120px; height: 110px; }
</style>
</head>
<body>

  <section class="sheet letterhead">
    <div class="brand"><span class="brand-dot"></span><span class="brand-name">Bright Harbor Learning</span></div>
    <div class="rule rule-top"></div>
    <p class="address">P.O. Box 518243<br>Dubai UAE</p>
    <p class="contact">Tel: (000) 0000 0000<br>Email: info@brightharborlearning.example</p>
    <div class="decor" role="img" aria-label="Faint decorative brand watermark"></div>
    <p class="web">www.brightharborlearning.example</p>
    <div class="rule rule-bottom"></div>
    <p class="legal">Bright Harbor Learning LLP operates as a limited liability partnership registered in England and Wales (with registered number OC742168).</p>
  </section>

  <section class="sheet card">
    <div class="brand"><span class="brand-dot"></span><span class="brand-name">Bright Harbor Learning</span></div>
    <p class="address">P.O. Box 518243<br>Dubai UAE</p>
    <div class="person">
      <p class="person-name">Name, Title</p>
      <p class="person-tel">Tel: (000) 0000 0000</p>
      <p class="person-email">info@brightharborlearning.example</p>
    </div>
    <p class="band">www.brightharborlearning.example</p>
  </section>

  <section class="sheet slip">
    <div class="decor" role="img" aria-label="Faint decorative brand watermark"></div>
    <p class="greeting">with <strong>compliments</strong></p>
    <div class="brand"><span class="brand-dot"></span><span class="brand-name">Bright Harbor Learning</span></div>
    <p class="legal">Bright Harbor Learning LLP operates as a limited liability partnership registered in England and Wales (with registered number OC742168).</p>
  </section>

  <section class="sheet envelope">
    <div class="brand"><span class="brand-dot"></span><span class="brand-name">Bright Harbor Learning</span></div>
    <p class="address">P.O. Box 518243<br>Dubai UAE</p>
    <div class="decor" role="img" aria-label="Faint decorative brand watermark"></div>
  </section>

</body>
</html>
```